Fence Flyer to Attract More Sales During Winter

We need a new flyer made that we can distribute to residential mailboxes. The flyer is to promote our Winter Fence Sale. We like simply designs, and we would like the flyer to showcase a lot of our fence photos. More of our photos are online at our website at www.mybrindlewoodfence.com - our new address needs to also be featured on the flyer - 574 Quarry rd, Monroe, NC 28117. I do want the words "WINTER FENCE SALE" to be dominate on the flyer with the description "Wood fences starting at $12/FT!" Please look through our Facebook page and our website to gather more photos or information. We are flexible on colors, nothing to fancy - simple flyer design please.

Target Market(s)

Residential homeowners that need a new fence to enclose their yard for safety, security or decorative

Industry/Entity Type

Residential Construction

Font styles to use
Sans Serif

Colors

Designer to choose colors to be used in the design.

Requirements
Must have
• Winter Fence Sale
• Contact information for the business
• "Come visit our outdoor showroom, open 24/7!"
Nice to have
• Photos of our fences - you can find more on our website at www.MyBrindlewoodFence.com or Facebook.com/MapleholtFenceWBT
Should not have
• Flashy designs

```html
<!DOCTYPE html>
<html lang="en">
<head>
<meta charset="UTF-8">
<title>Winter Fence Sale Flyer</title>
<link href="https://fonts.googleapis.com/css2?family=Poppins:wght@500;600;700&display=swap" rel="stylesheet">
<style>
  :root {
    --red: #f0141c;
    --red-deep: #d20a12;
    --red-glow: #ff3b3f;
    --white: #ffffff;
    --yellow: #fff200;
    --wood: #c9a57a;
    --wood-dark: #8d6c48;
    --leaf: #3f6a2e;
    --leaf-light: #7aa35a;
    --soil: #b8643a;
    --sky: #c9d3d8;
  }
  * { margin: 0; padding: 0; box-sizing: border-box; }
  html, body { width: 927px; height: 1200px; overflow: hidden; background: var(--white); }
  body { font-family: 'Poppins', sans-serif; }
  .flyer { position: relative; width: 927px; height: 1200px; overflow: hidden; }

  .photo { position: absolute; }
  .photo--wood { background: linear-gradient(160deg, var(--leaf) 0%, var(--wood) 45%, var(--wood-dark) 100%); }
  .photo--wood-soft { background: linear-gradient(180deg, var(--leaf) 0%, #d8c4a2 40%, var(--wood-dark) 100%); }
  .photo--metal { background: linear-gradient(180deg, var(--leaf) 0%, #4a5a3a 45%, var(--soil) 100%); }
  .photo--metal-sky { background: linear-gradient(180deg, var(--sky) 0%, var(--leaf) 35%, var(--soil) 100%); }
  .photo--garden { background: linear-gradient(180deg, var(--leaf) 0%, var(--leaf-light) 60%, #3c5a2a 100%); }

  .sale-panel {
    position: absolute; left: 250px; top: 299px; width: 427px; height: 901px; overflow: hidden;
    background: radial-gradient(circle at 50% 30%, var(--red-glow) 0%, var(--red) 45%, var(--red-deep) 100%);
    color: var(--white); text-align: center;
  }
  .headline-frame {
    position: absolute; left: 33px; top: 31px; width: 362px; height: 322px;
    border: 5px solid var(--white); border-bottom: none;
  }
  .frame-base { position: absolute; top: 350px; height: 5px; background: var(--white); }
  .frame-base--left { left: 33px; width: 100px; }
  .frame-base--right { left: 285px; width: 110px; }
  .frame-label {
    position: absolute; left: 0; right: 0; top: 341px;
    font-size: 15px; font-weight: 600; letter-spacing: 0.5px;
  }
  .headline { position: absolute; left: 0; right: 0; font-weight: 700; line-height: 1; }
  .headline--winter { top: 83px; font-size: 78px; }
  .headline--fence { top: 172px; font-size: 78px; }
  .headline--sale { top: 254px; font-size: 46px; color: var(--yellow); }

  .line { position: absolute; left: 0; right: 0; font-weight: 700; line-height: 1; }
  .offer-lead { top: 368px; font-size: 41px; }
  .offer-price { top: 412px; font-size: 78px; color: var(--yellow); }
  .visit-come { top: 525px; font-size: 64px; color: var(--yellow); }
  .visit-our { top: 583px; font-size: 40px; }
  .visit-place { top: 628px; font-size: 17px; color: var(--yellow); }

  .hours {
    position: absolute; left: 0; right: 0; top: 700px;
    display: flex; align-items: center; justify-content: center; gap: 12px;
    font-size: 33px; font-weight: 700; line-height: 1;
  }
  .hours::before, .hours::after { content: ""; width: 38px; height: 2px; background: var(--white); }

  .contact { position: absolute; left: 35px; right: 20px; top: 0; height: 0; text-align: left; }
  .contact-row { position: absolute; left: 0; display: flex; align-items: center; gap: 16px; white-space: nowrap; }
  .contact-row svg { flex: none; }
  .contact-email { top: 728px; font-size: 17px; font-weight: 600; line-height: 26px; }
  .contact-phone { top: 758px; font-size: 45px; font-weight: 700; line-height: 54px; }
  .contact-address { top: 828px; font-size: 18.5px; font-weight: 600; line-height: 26px; }
</style>
</head>
<body>
<div class="flyer">
  <div class="photo photo--wood" style="left:0;top:0;width:250px;height:299px" role="img" aria-label="Photo of a long new wooden privacy fence along a gravel path"></div>
  <div class="photo photo--garden" style="left:250px;top:0;width:427px;height:299px" role="img" aria-label="Photo of a wooden picket section beside a black metal garden gate with patio table"></div>
  <div class="photo photo--metal" style="left:677px;top:0;width:250px;height:299px" role="img" aria-label="Photo of a black aluminum fence around a backyard with a wooden deck stair"></div>

  <div class="photo photo--wood-soft" style="left:0;top:300px;width:250px;height:298px" role="img" aria-label="Photo of a dog-ear wooden picket fence with a gate beside a house"></div>
  <div class="photo photo--metal" style="left:677px;top:300px;width:250px;height:298px" role="img" aria-label="Photo of a black aluminum fence on a sloped yard lined with evergreens"></div>

  <div class="photo photo--wood-soft" style="left:0;top:600px;width:250px;height:298px" role="img" aria-label="Photo of a spaced wooden picket fence along a wooded yard"></div>
  <div class="photo photo--metal-sky" style="left:677px;top:600px;width:250px;height:298px" role="img" aria-label="Photo of a black metal fence around a new lot under a cloudy sky"></div>

  <div class="photo photo--wood" style="left:0;top:900px;width:250px;height:300px" role="img" aria-label="Photo of a scalloped wooden fence in a sunny backyard"></div>
  <div class="photo photo--garden" style="left:677px;top:900px;width:250px;height:300px" role="img" aria-label="Photo of a black aluminum fence and gate around a landscaped garden"></div>

  <section class="sale-panel">
    <div class="headline-frame"></div>
    <div class="frame-base frame-base--left"></div>
    <div class="frame-base frame-base--right"></div>
    <h1 class="headline headline--winter">WINTER</h1>
    <div class="headline headline--fence">FENCE</div>
    <div class="headline headline--sale">SALE</div>
    <div class="frame-label">WOOD FENCES</div>

    <div class="line offer-lead">STARTING AT</div>
    <div class="line offer-price">$12/FT!</div>

    <div class="line visit-come">COME</div>
    <div class="line visit-our">VISIT OUR</div>
    <div class="line visit-place">OUTDOOR SHOWROOM</div>

    <div class="hours">OPEN 24/7</div>

    <div class="contact">
      <div class="contact-row contact-email">
        <svg width="20" height="14" viewBox="0 0 20 14"><rect x="0" y="0" width="20" height="14" fill="var(--yellow)"/><path d="M0 0 L10 8 L20 0" fill="none" stroke="var(--red)" stroke-width="1.6"/></svg>
        <span>OFFICE@MYBRINDLEWOODFENCE.COM</span>
      </div>
      <div class="contact-row contact-phone">
        <svg width="20" height="22" viewBox="0 0 20 22"><path d="M4 2 C2 3 1 6 3 10 C5 15 9 19 13 20 C16 21 18 19 18 17 L14 14 L11 16 C9 15 6 12 5 9 L7 6 Z" fill="var(--yellow)"/></svg>
        <span>704-555-0186</span>
      </div>
      <div class="contact-row contact-address">
        <svg width="20" height="24" viewBox="0 0 20 24"><path d="M10 0 C4.5 0 1 4 1 9 C1 15 10 24 10 24 C10 24 19 15 19 9 C19 4 15.5 0 10 0 Z" fill="var(--yellow)"/><circle cx="10" cy="9" r="3.5" fill="var(--red)"/></svg>
        <span>574 QUARRY RD, MONROE, NC 28117</span>
      </div>
    </div>
  </section>
</div>
</body>
</html>
```